Double-sided business card needed - specific brief

We need a double sided business card designed for our company Radiant Trimline. Having lost a lot of weight myself, the back of the card needs to show my before and after pictures. It needs to cover the entire back side of the card. This might be with my two before pictures over set on top of my main after picture or in separate frames. I'll leave that to your artistic consideration. The front needs to have our logo with contact details centred below.

The cards will be printed by PRINTKO.com and will be rectangular, 84mm x 55mm, but with ROUNDED edges. Please therefore present your designs rectangular but with rounded edges if possible.

The card should be designed in LANDSCAPE orientation.

As well as the logo, the front of the card should have the following details:

Moira Blakewell
Weight Loss Motivator with 189lb personal loss
moira@radiant-trimline.example
+44 (0)7700 900418

The website is important so should perhaps be more bold than the rest:
www.radiant-trimline.example

My brand colours are: Pink #CD2366, Light Pink #FD88AD. Blue #1C9CB1, Light Blue #64C4DE

Target Market(s)

Women 30+

Contact Information for Business Card

As description above

Font styles to use
Sans Serif

Requirements
Must have
• Double sided.
• Back side entirely covered with my before and after pictures.
• You may wish to float my before pictures on top of my after picture or add them in different frames. I look forward to seeing your different suggestions.

```html
<!DOCTYPE html>
<html lang="en">
<head>
<meta charset="utf-8">
<title>Radiant Trimline – Business Card</title>
<link href="https://fonts.googleapis.com/css2?family=Didact+Gothic&family=Mulish:wght@700;800&display=swap" rel="stylesheet">
<style>
  :root{
    --pink:#CD2366;
    --light-pink:#FD88AD;
    --blue:#1C9CB1;
    --light-blue:#64C4DE;
    --paper:#ffffff;
    --backdrop:#efeae3;
    --before-green:#6f8f4e;
    --before-light:#c9cfb6;
    --after-navy:#2c3550;
    --after-cream:#d9d2c4;
  }
  *{box-sizing:border-box;margin:0;padding:0}
  html,body{width:1200px;height:960px;overflow:hidden}
  body{
    background:var(--backdrop);
    font-family:"Didact Gothic",sans-serif;
    position:relative;
  }
  .card{
    position:absolute;
    left:280px;
    width:640px;height:419px;
    border-radius:18px;
    overflow:hidden;
    background:var(--paper);
    box-shadow:0 6px 20px rgba(0,0,0,.15);
  }
  .card--front{top:41px}
  .card--back{top:500px}

  /* front */
  .brand{
    position:absolute;top:58px;left:0;right:0;
    display:flex;justify-content:center;align-items:center;gap:14px;
  }
  .brand__dot{width:34px;height:34px;border-radius:50%;background:var(--light-blue)}
  .brand__name{
    font-family:"Didact Gothic",sans-serif;
    font-size:38px;letter-spacing:1px;color:var(--pink);
  }
  .person{position:absolute;left:64px;top:160px}
  .person__name{font-size:28px;color:var(--pink);letter-spacing:.5px;text-transform:uppercase}
  .person__role{margin-top:18px;font-size:16px;color:var(--pink);line-height:1.5}
  .person__role .figure{font-size:23px;color:var(--blue)}
  .divider{position:absolute;left:318px;top:188px;width:2px;height:104px;background:var(--pink)}
  .contact{position:absolute;left:340px;top:206px;list-style:none}
  .contact li{display:flex;align-items:center;gap:12px;font-size:15.5px;color:var(--pink);margin-bottom:14px}
  .contact svg{flex:none}
  .website{
    position:absolute;left:0;right:0;top:318px;text-align:center;
    font-family:"Mulish",sans-serif;font-weight:800;font-size:24px;color:var(--pink);
    letter-spacing:.5px;
  }
  .waves{position:absolute;left:0;bottom:0}

  /* back */
  .photos{position:absolute;inset:0}
  .photo-label{
    position:absolute;font-size:22px;color:var(--light-blue);
    text-shadow:0 1px 2px rgba(0,0,0,.5);
  }
  .photo-label--before{left:250px;top:370px}
  .photo-label--after{right:40px;top:370px}
</style>
</head>
<body>

<section class="card card--front" aria-label="Card front">
  <div class="brand">
    <span class="brand__dot"></span>
    <span class="brand__name">Radiant Trimline</span>
  </div>

  <div class="person">
    <h1 class="person__name">Moira Blakewell</h1>
    <p class="person__role">Weight Loss Motivator with<br><span class="figure">189lb</span> personal loss</p>
  </div>

  <div class="divider"></div>

  <ul class="contact">
    <li>
      <svg width="16" height="12" viewBox="0 0 16 12"><rect x="0.5" y="0.5" width="15" height="11" rx="1" fill="var(--light-blue)"/><path d="M1 1l7 6 7-6" stroke="#fff" stroke-width="1.4" fill="none"/></svg>
      moira@radiant-trimline.example
    </li>
    <li>
      <svg width="16" height="16" viewBox="0 0 24 24"><path fill="var(--light-blue)" d="M6.6 10.8a15.1 15.1 0 006.6 6.6l2.2-2.2a1 1 0 011-.25 11.4 11.4 0 003.6.57 1 1 0 011 1V20a1 1 0 01-1 1A17 17 0 013 4a1 1 0 011-1h3.5a1 1 0 011 1c0 1.25.2 2.45.57 3.57a1 1 0 01-.25 1z"/></svg>
      +44 (0)7700 900418
    </li>
  </ul>

  <p class="website">www.radiant-trimline.example</p>

  <svg class="waves" width="640" height="110" viewBox="0 0 640 110" aria-hidden="true">
    <path d="M0 28 C180 40 380 50 640 92 L640 110 L0 110Z" fill="var(--light-blue)"/>
    <path d="M0 40 C180 50 380 62 640 100 L640 110 L0 110Z" fill="var(--paper)"/>
    <path d="M0 46 C180 56 380 70 640 104 L640 110 L0 110Z" fill="var(--pink)"/>
  </svg>
</section>

<section class="card card--back" aria-label="Card back">
  <svg class="photos" width="640" height="419" viewBox="0 0 640 419">
    <defs>
      <linearGradient id="beforeTone" x1="0" y1="0" x2="0" y2="1">
        <stop offset="0" stop-color="var(--before-light)"/>
        <stop offset=".45" stop-color="var(--before-green)"/>
        <stop offset="1" stop-color="#5d7f3f"/>
      </linearGradient>
      <linearGradient id="afterTone" x1="0" y1="0" x2="1" y2="1">
        <stop offset="0" stop-color="var(--after-cream)"/>
        <stop offset=".6" stop-color="var(--after-navy)"/>
        <stop offset="1" stop-color="#6a3a35"/>
      </linearGradient>
    </defs>
    <polygon points="0,0 360,0 440,419 0,419" fill="url(#beforeTone)" role="img" aria-label="Before photo: Moira standing in a garden holding a cat"/>
    <polygon points="364,0 640,0 640,419 444,419" fill="url(#afterTone)" role="img" aria-label="After photo: Moira seated on a leather armchair indoors"/>
    <line x1="362" y1="0" x2="442" y2="419" stroke="#fff" stroke-width="4"/>
  </svg>
  <span class="photo-label photo-label--before">Before</span>
  <span class="photo-label photo-label--after">After</span>
</section>

</body>
</html>
```